Manuka honey wholesales and export company needs a website

We are a Manuka honey Wholesale and export company based in New Zealand and needing a website to attract new clients.
We produce one of the worlds best honeys so we need a clean, modern look that lets everybody know that we can supply our product around the world.
We source only the finest Manuka honey from some of the most remote parts of New Zealand and send it around the world for everyone to enjoy.
We need a website that will allow people to inquire about export or bulk purchasing as well as a buying tab with pricing but one that we can add photos to as our product labels are not complete yet.
We also support and supply local farmers markets and a page dedicated to this would be good with details on when and where they are.

Here are links to other manuka honey websites to get an idea
http://www.hivelarkfields.co.nz/
http://www.pellora.co.nz/key-ingredients/manuka-honey/nz100008?gclid=Xq7PLmRtYvBNsKdWoEjZaHuFcGiTeLpOyNbRkVwQmXsDaJzUoKiHnCtFgPlEbYrAqMdSvZuWxTeNoGjHkLrPfIsBaCqZyDm

Target Market(s)

The general public, retail shops and exporters

Industry/Entity Type

Health And Wellness

Number of Pages Required

5+ page

Font styles to use
Serif

Requirements
Must have
• 1. A page and contact details for Export and wholesale inquiries
• Desmond Harlow
• Export manager
• +64 21 438 190
• dkharlow@pelmail.co.nz
• 2. Page for the farmers market we supply our product to.
• Details....
• Contact: Neil Forbes
• +64 21 067 4183
• tideflowernz@mailpost.com
• MARKET INFORMATION
• Quaywell Market
• The market operates year round and is located on Ferndell Square.*
• http://quaywell.org/sol-verde-market/
• Saturday 8am-1pm
• Sunday 9am-1pm
• Ashgrove Hamlet Market
• http://www.ashgrovegrowersmarket.co.nz/
• 64 Paddock Ln, Oakhurst, Auckland 2469, New Zealand
• Market is held each Sunday from 8:30am-1pm.
• 3. An information page on manuka honey....i will attach info but most of the info you can find on other manuka honey websites..
• Health benefits..
• There are two main components of Manuka honey which give it many health benefits:
• - Hydrogen peroxide, a naturally antibiotic found in Manuka honey.
• - Methylglyoxal (MG). A powerful antibiotic compound found in large quantities in Manuka honey.
• What is MGO?
• The MGO indicates the amount of Methylglyoxal in the honey. The higher the MGO rating the more antibacterial properties are in the honey.
• Proven health Benefits of Active Manuka are....
• Aiding in the treatment of:
• - -Common Cold and Flu
• - -sore throats
• - -cuts and abrasions
• - -Reduce hair loss and scalp problems
• - -treating fungal infections
• - -Burns
• - -ulsers
• - -strengthening the immune system
• 4. A product page with a range of our products with a link yo by direct from us
• The details for this page will need to be added later as we are still doing our range!
Nice to have
• Feel free to make up a mission statement or whatever inspires you to make this a great website.
Should not have
• Go crazy please! I trust you will come up with something amazing :)

```html
<!DOCTYPE html>
<html lang="en">
<head>
<meta charset="utf-8">
<title>Tidebloom Honey NZ Limited — Manuka Honey</title>
<link href="https://fonts.googleapis.com/css2?family=Montserrat:wght@400;600;700&family=Open+Sans:wght@400;600&display=swap" rel="stylesheet">
<style>
:root{
  --honey:#f2c200;
  --honey-deep:#e3b000;
  --ink:#1f1f1f;
  --text:#3a3a3a;
  --muted:#6b6b6b;
  --paper:#ffffff;
  --mist:#e9e9ea;
  --night:#262626;
  --night-2:#2e2e2e;
  --line:#444;
}
*{box-sizing:border-box;margin:0;padding:0}
html,body{width:1200px;height:4800px;overflow:hidden}
body{position:relative;background:var(--paper);font-family:"Open Sans",Arial,sans-serif;color:var(--text)}
.abs{position:absolute}
.heading{font-family:"Montserrat",Arial,sans-serif;font-weight:700;letter-spacing:2px;text-transform:uppercase}
.btn{position:absolute;background:var(--honey);color:var(--ink);font-family:"Montserrat",Arial,sans-serif;font-weight:600;font-size:15px;display:flex;align-items:center;justify-content:center;text-transform:uppercase;border-radius:3px}

/* Hero */
.hero{left:0;top:0;width:1200px;height:730px;background:radial-gradient(ellipse at 40% 60%,#8a6a3c 0%,#4d3820 45%,#241a10 100%)}
.hero-shade{left:0;top:0;width:1200px;height:730px;background:linear-gradient(180deg,rgba(0,0,0,.35),rgba(0,0,0,.15) 50%,rgba(0,0,0,.45))}
.brand{left:125px;top:26px;width:280px;display:flex;flex-direction:column;align-items:center;gap:10px;color:var(--paper);font-family:"Montserrat",Arial,sans-serif;font-weight:600;font-size:17px;white-space:nowrap}
.brand-dot{width:52px;height:52px;border-radius:50%;background:var(--honey)}
.nav{right:124px;top:28px;display:flex;gap:6px;align-items:center}
.nav a{font-family:"Montserrat",Arial,sans-serif;font-size:12px;font-weight:600;color:var(--paper);text-decoration:none;padding:8px 12px;text-transform:uppercase;white-space:nowrap}
.nav a.active{background:var(--honey);color:var(--ink)}
.cart{width:32px;height:32px;background:var(--honey);position:relative;margin-left:8px}
.cart span{position:absolute;right:-8px;top:-8px;width:16px;height:16px;border-radius:50%;background:var(--paper);color:var(--ink);font-size:10px;display:flex;align-items:center;justify-content:center}
.hero-title{left:0;top:350px;width:1200px;text-align:center;color:var(--paper);font-size:62px;letter-spacing:10px}
.hero-title .accent{color:var(--honey)}
.hero-sub{left:0;top:432px;width:1200px;text-align:center;color:var(--paper);font-family:"Montserrat",Arial,sans-serif;font-weight:600;font-size:16px;letter-spacing:4px}
.dots{left:550px;top:660px;display:flex;gap:12px}
.dots i{width:9px;height:9px;border-radius:50%;background:var(--paper);opacity:.8}

/* About */
.hexes{left:150px;top:760px;width:460px;height:470px}
.about{left:700px;top:820px;width:320px;text-align:center}
.section-title{color:var(--honey);font-size:30px}
.about p{font-size:14px;line-height:1.7;margin-top:20px}
.about strong{color:var(--ink)}

/* Health */
.health{left:0;top:1280px;width:1200px;height:1000px;background:var(--mist)}
.health-title{left:0;top:1325px;width:1200px;text-align:center}
.health-title .sub{font-family:"Montserrat",Arial,sans-serif;color:var(--ink);font-size:28px;letter-spacing:1px;margin-top:14px}
.benefit{position:absolute;width:480px;height:130px;display:flex;align-items:center;gap:30px}
.benefit-img{width:110px;height:124px;flex:none;position:relative;clip-path:polygon(50% 0,100% 25%,100% 75%,50% 100%,0 75%,0 25%)}
.benefit-num{position:absolute;width:40px;height:28px;left:35px;bottom:10px;background:var(--honey);color:var(--ink);font-size:12px;font-weight:600;display:flex;align-items:center;justify-content:center}
.benefit p{font-size:14px;line-height:1.65;width:320px;color:var(--text)}

/* MGO */
.mgo-img{left:300px;top:2280px;width:230px;height:420px;background:radial-gradient(ellipse at 50% 78%,#e7a21a 0%,#d78a08 35%,#f5d08a 60%,#fff 78%)}
.mgo{left:580px;top:2400px;width:520px}
.mgo p{font-size:14px;line-height:1.6;margin-top:18px}

/* Products */
.products{left:0;top:2760px;width:1200px;height:580px;background:var(--mist)}
.products-title{left:0;top:2822px;width:1200px;text-align:center}
.product{position:absolute;top:2920px;width:240px;text-align:center}
.jar{margin:0 auto;width:130px;height:220px;border-radius:14px}
.product h3{font-family:"Montserrat",Arial,sans-serif;font-size:15px;font-weight:600;color:var(--ink);margin-top:34px}
.buy{display:flex;justify-content:center;align-items:center;gap:18px;margin-top:20px}
.add{background:var(--honey);color:var(--ink);font-size:11px;font-weight:600;padding:8px 10px;font-family:"Montserrat",Arial,sans-serif}
.price{font-size:13px;line-height:1.25;text-align:left;color:var(--ink)}
.price s{color:var(--muted);display:block}

/* Difference */
.diff{left:130px;top:3440px;width:420px;text-align:center}
.diff p{font-size:14px;line-height:1.7;margin-top:28px}
.video{left:600px;top:3434px;width:468px;height:262px;background:linear-gradient(135deg,#6d4e2a,#b8893f 55%,#5a4226)}
.video-label{left:620px;top:3448px;color:var(--paper);font-family:"Montserrat",Arial,sans-serif;font-weight:600;font-size:14px;text-transform:uppercase}

/* Components band */
.band{left:0;top:3776px;width:1200px;height:496px;background:linear-gradient(90deg,#f7cf00 0%,#f3bd00 45%,#e8a700 70%,#f4c600 100%)}
.component{left:160px;width:420px;color:var(--ink)}
.component h3{font-size:24px;letter-spacing:1px}
.component p{font-size:17px;line-height:1.45;margin-top:16px}
.band-rule{left:160px;top:4008px;width:430px;height:1px;background:rgba(0,0,0,.35)}

/* Footer */
.footer{left:0;top:4272px;width:1200px;height:528px;background:var(--night)}
.fcol{top:4340px;width:240px;color:#cfcfcf;font-size:13px}
.fcol h4{font-family:"Montserrat",Arial,sans-serif;font-size:12px;font-weight:700;color:var(--paper);letter-spacing:1px;margin-bottom:20px;text-transform:uppercase}
.fcol li{list-style:none;display:flex;align-items:center;gap:10px;margin-bottom:14px}
.fcol svg{flex:none}
.frule{left:128px;top:4475px;width:944px;height:1px;background:var(--line)}
.fbrand{left:170px;top:4525px;width:320px;display:flex;flex-direction:column;align-items:center;color:var(--paper);font-family:"Montserrat",Arial,sans-serif;font-weight:600;font-size:20px;white-space:nowrap}
.fbrand .brand-dot{margin:0 0 16px;width:60px;height:60px}
.fmenu{left:630px;top:4560px;color:#cfcfcf;font-size:12px}
.fmenu h4{font-family:"Montserrat",Arial,sans-serif;font-size:12px;color:var(--honey);margin-bottom:14px}
.fmenu .links{display:flex;gap:10px}
.follow{left:630px;top:4640px;display:flex;align-items:center;gap:12px;color:var(--honey);font-family:"Montserrat",Arial,sans-serif;font-weight:700;font-size:12px}
.follow i{width:28px;height:28px;border-radius:50%;background:#555}
.copy{left:0;top:4762px;width:1200px;text-align:center;color:#9a9a9a;font-size:11px}
</style>
</head>
<body>

<!-- Hero -->
<div class="abs hero" role="img" aria-label="Close-up photo of a beekeeper lifting a honeycomb frame covered with bees"></div>
<div class="abs hero-shade"></div>
<div class="abs brand"><div class="brand-dot"></div>Tidebloom Honey NZ Limited</div>
<nav class="abs nav">
  <a class="active">Home</a><a>About us</a><a>Process</a><a>Honey</a><a>Products</a><a>Contact us</a>
  <div class="cart"><span>0</span></div>
</nav>
<h1 class="abs heading hero-title">Manuka H<span class="accent">o</span>ney</h1>
<div class="abs hero-sub">WHOLESALE AND EXPORT IN NEW ZEALAND</div>
<div class="abs dots"><i></i><i></i><i></i><i></i><i></i></div>

<!-- About -->
<svg class="abs hexes" viewBox="0 0 460 470" aria-hidden="true">
  <g fill="#f2c200">
    <polygon points="228,0 328,56 328,170 228,226 128,170 128,56"/>
    <polygon points="128,244 228,300 228,414 128,470 28,414 28,300"/>
    <polygon points="324,244 424,300 424,414 324,470 224,414 224,300"/>
  </g>
  <g fill="#1f1f1f">
    <path d="M228 50 C212 74 206 86 206 98 a22 22 0 0 0 44 0 C250 86 244 74 228 50Z"/>
    <rect x="88" y="318" width="50" height="32" rx="3"/>
    <path d="M140 326 h18 l12 14 v10 h-30z"/>
    <circle cx="102" cy="354" r="7"/><circle cx="155" cy="354" r="7"/>
    <circle cx="324" cy="336" r="26" fill="none" stroke="#1f1f1f" stroke-width="5"/>
    <path d="M311 336 l9 9 l17 -18" fill="none" stroke="#1f1f1f" stroke-width="5"/>
  </g>
  <g font-family="Montserrat, Arial, sans-serif" font-size="14" fill="#1f1f1f" text-anchor="middle" font-weight="600">
    <text x="228" y="160">EXTRACTION</text>
    <text x="128" y="404">FREE SHIPPING</text>
    <text x="324" y="404">QUALITY</text>
  </g>
</svg>
<section class="abs about">
  <h2 class="heading section-title">About us</h2>
  <p><strong>We are Manuka honey Wholesale and export company based in New Zealand.</strong></p>
  <p>We produce one of the worlds best honeys so we need a clean, modern look that lets everybody know that we can supply our product around the world.</p>
</section>
<div class="btn" style="left:790px;top:1098px;width:130px;height:46px">Read more</div>

<!-- Health benefits -->
<div class="abs health"></div>
<div class="abs health-title">
  <h2 class="heading section-title">Health benefits of</h2>
  <div class="sub">MANUKA HONEY</div>
</div>

<div class="benefit" style="left:160px;top:1440px"><div class="benefit-img" role="img" aria-label="Jar of honey with dipper" style="background:linear-gradient(#d99a1a,#8a5a12)"><div class="benefit-num">01</div></div><p>Medical grade Manuka honey used on post operative wounds was more effective than regular antibiotic creams.</p></div>
<div class="benefit" style="left:680px;top:1440px"><div class="benefit-img" role="img" aria-label="Honey pouring into a bowl" style="background:linear-gradient(#f0b640,#b9761a)"><div class="benefit-num">02</div></div><p>Manka Honey can fight bacterial sickness (c.Diff) and diarrhea.</p></div>

<div class="benefit" style="left:160px;top:1600px"><div class="benefit-img" role="img" aria-label="Portrait photo showing clear skin" style="background:linear-gradient(#c89a7e,#7a5040)"><div class="benefit-num">03</div></div><p>The unique antibacterial and antimicrobial properties in Manuka Honey can help with Eczema and Acne.</p></div>
<div class="benefit" style="left:680px;top:1600px"><div class="benefit-img" role="img" aria-label="Person with seasonal allergy sneezing" style="background:linear-gradient(#d8d8d8,#8c8c8c)"><div class="benefit-num">04</div></div><p>Seasonal allergy symptoms can be reduced using Manuka Honey.</p></div>

<div class="benefit" style="left:160px;top:1760px"><div class="benefit-img" role="img" aria-label="Hands resting on stomach" style="background:linear-gradient(#b9c2cc,#6c7686)"><div class="benefit-num">05</div></div><p>Manuka Honey can help heal Intestinal Lining and prevent future damage.</p></div>
<div class="benefit" style="left:680px;top:1760px"><div class="benefit-img" role="img" aria-label="Healthy smile with white teeth" style="background:linear-gradient(#f2d3c4,#c6786a)"><div class="benefit-num">06</div></div><p>New zealand research showed at 35% reduction in plaque and Manuka Honey can help prevent Gingivitis and Tooth decay.</p></div>

<div class="benefit" style="left:160px;top:1920px"><div class="benefit-img" role="img" aria-label="Microscope view of bacteria" style="background:linear-gradient(#e4b6b8,#b86e76)"><div class="benefit-num">07</div></div><p>Manuka Honey is effective against Staph and the Superbug MRSA.</p></div>
<div class="benefit" style="left:680px;top:1920px"><div class="benefit-img" role="img" aria-label="Person holding a sore throat" style="background:linear-gradient(#d0d0d0,#7c7c7c)"><div class="benefit-num">08</div></div><p>The Ferncliff Cancer Institute approves of Manuka Honey to treat sore throats caused by chemotherapy.</p></div>

<div class="benefit" style="left:160px;top:2085px"><div class="benefit-img" role="img" aria-label="Glass of milk with honey" style="background:linear-gradient(#f6e6c0,#d69a30)"><div class="benefit-num">09</div></div><p>Milk and Manuka Honey can aid your sleep as it boosts melatnin levels.</p></div>
<div class="benefit" style="left:680px;top:2085px"><div class="benefit-img" role="img" aria-label="Person resting with stomach ache" style="background:linear-gradient(#a6dcea,#3f9fb8)"><div class="benefit-num">10</div></div><p>Stomach ulcers and be healed with Manuka Honey and it can kill H.Pylori, the bacteria responsible for most ulcers.</p></div>

<!-- MGO -->
<div class="abs mgo-img" role="img" aria-label="Golden honey dripping from a dipper into a pool"></div>
<section class="abs mgo">
  <h2 class="heading section-title">What is MGO?</h2>
  <p>The MGO indicates the amount of Methylglyoxal in the honey.</p>
  <p style="margin-top:10px">The higher the MGO rating the more antibacterial properties are in the honey.</p>
</section>
<div class="btn" style="left:580px;top:2570px;width:130px;height:46px">Read more</div>

<!-- Products -->
<div class="abs products"></div>
<h2 class="abs heading section-title products-title">Our products</h2>
<div class="product" style="left:94px"><div class="jar" role="img" aria-label="Dark jar of manuka honey with black label" style="background:linear-gradient(90deg,#3a1a10,#7a3a1c 50%,#2a120a)"></div><h3>HEADING 1</h3><div class="buy"><span class="add">ADD TO CART</span><span class="price"><s>$15.00</s>$10.00</span></div></div>
<div class="product" style="left:350px"><div class="jar" role="img" aria-label="Clear jar of golden honey" style="background:linear-gradient(90deg,#d08f10,#f4c24a 50%,#c9860c)"></div><h3>HEADING 2</h3><div class="buy"><span class="add">ADD TO CART</span><span class="price"><s>$15.00</s>$10.00</span></div></div>
<div class="product" style="left:603px"><div class="jar" role="img" aria-label="Honey jar with blank white label" style="background:linear-gradient(180deg,#d7a431 0 30%,#f4f1ea 30% 75%,#d7a431 75%)"></div><h3>HEADING 3</h3><div class="buy"><span class="add">ADD TO CART</span><span class="price"><s>$15.00</s>$10.00</span></div></div>
<div class="product" style="left:856px"><div class="jar" role="img" aria-label="Amber honey jar with cream label" style="background:linear-gradient(90deg,#7a2e10,#b85a24 50%,#6a260c)"></div><h3>HEADING 4</h3><div class="buy"><span class="add">ADD TO CART</span><span class="price"><s>$15.00</s>$10.00</span></div></div>

<!-- Our difference -->
<section class="abs diff">
  <h2 class="heading section-title">Our difference</h2>
  <p>We also support and supply local farmers markets and a page dedicated to this would be good with details on when and where they are</p>
</section>
<div class="btn" style="left:246px;top:3628px;width:190px;height:46px">Watch our videos</div>
<div class="abs video" role="img" aria-label="Video still of a beekeeper holding a honeycomb frame"></div>
<div class="abs video-label">Video heading 1</div>
<svg class="abs" style="left:798px;top:3530px" width="72" height="62" viewBox="0 0 72 62" aria-hidden="true"><rect width="72" height="62" rx="6" fill="#f2c200"/><polygon points="28,18 50,31 28,44" fill="#1f1f1f"/></svg>

<!-- Components band -->
<div class="abs band" role="img" aria-label="Photo of a bee on a bright yellow flower"></div>
<div class="abs component" style="top:3868px"><h3 class="heading">Hydrogen peroxide</h3><p>A naturally antibiotic found in Manuka honey</p></div>
<div class="abs band-rule"></div>
<div class="abs component" style="top:4060px"><h3 class="heading">Methylglyoxal (MG).</h3><p>A powerful antibiotic compound found in large quantities in Manuka honey.</p></div>

<!-- Footer -->
<footer>
<div class="abs footer"></div>
<div class="abs fcol" style="left:128px"><h4>Export and wholesale</h4><ul>
  <li><svg width="14" height="14" viewBox="0 0 24 24"><path fill="#f2c200" d="M6.6 10.8a15 15 0 0 0 6.6 6.6l2.2-2.2a1 1 0 0 1 1-.25 11.4 11.4 0 0 0 3.6.57 1 1 0 0 1 1 1V20a1 1 0 0 1-1 1A17 17 0 0 1 3 4a1 1 0 0 1 1-1h3.5a1 1 0 0 1 1 1c0 1.250.2 2.45.57 3.6a1 1 0 0 1-.25 1z"/></svg>+64 21 438 190</li>
  <li><svg width="14" height="12" viewBox="0 0 24 20"><rect x="1" y="1" width="22" height="18" fill="none" stroke="#f2c200" stroke-width="2"/><path d="M1 1l11 9 11-9" fill="none" stroke="#f2c200" stroke-width="2"/></svg>dkharlow@pelmail.co.nz</li></ul></div>
<div class="abs fcol" style="left:390px"><h4>Farmers market</h4><ul>
  <li><svg width="14" height="14" viewBox="0 0 24 24"><path fill="#f2c200" d="M6.6 10.8a15 15 0 0 0 6.6 6.6l2.2-2.2a1 1 0 0 1 1-.25 11.4 11.4 0 0 0 3.6.57 1 1 0 0 1 1 1V20a1 1 0 0 1-1 1A17 17 0 0 1 3 4a1 1 0 0 1 1-1h3.5a1 1 0 0 1 1 1c0 1.25.2 2.45.57 3.6a1 1 0 0 1-.25 1z"/></svg>+64 21 067 4183</li>
  <li><svg width="14" height="12" viewBox="0 0 24 20"><rect x="1" y="1" width="22" height="18" fill="none" stroke="#f2c200" stroke-width="2"/><path d="M1 1l11 9 11-9" fill="none" stroke="#f2c200" stroke-width="2"/></svg>tideflowernz@mailpost.com</li></ul></div>
<div class="abs fcol" style="left:675px"><h4>Office hours</h4><ul><li>Saturday 8am-1pm</li><li>Sunday 9am-1pm</li></ul></div>
<div class="abs fcol" style="left:902px;width:190px"><h4>Contact us</h4><ul><li style="align-items:flex-start;line-height:1.6">64 Paddock Ln, Oakhurst, Auckland 2469, New Zealand</li></ul></div>
<div class="abs frule"></div>
<div class="abs fbrand"><div class="brand-dot"></div>Tidebloom Honey NZ Limited</div>
<div class="abs fmenu"><h4>MENU</h4><div class="links"><span>Home</span>/<span>About us</span>/<span>Process</span>/<span>Honey</span>/<span>Products</span>/<span>Contact Us</span></div></div>
<div class="abs follow">FOLLOW US :<i></i><i></i><i></i></div>
<div class="abs copy">Copyright © 2017 All Rights Reserved</div>
</footer>

</body>
</html>
```